Professional stationery for boutique management consulting business

I need branded business stationery for my consulting business, using our existing logo and website branding. We consult to senior executives to create deep cultural change needed for humane, people-centred workplaces. The key deliverables are: (A4 size) business letterheads, proposal cover, project folder, report template, email footer, business card, simple powerpoint template. A warm, empowering and expert tone of voice is important as it needs to bridge the gap between academia and industry. It should be clean and professional without feeling "over-branded".
I would like to see stationery designs that use my website colours and design elements (see attached file), especially the delta logo. Our fonts are Operetta and Sofia Pro.
Updates

Thanks for the designs sent so far. Just to confirm that our key deliverables for this project are: - (A4 size) business letterhead - (A4 size) proposal template - (A4 size) report template - Project folder, - Simple powerpoint template - Business card Many thanks

Target Market(s)

Senior executives and business professionals with an interest in business school thinking.

Industry/Entity Type

Management consulting and executive coaching

Font styles to use
Other font styles liked:
• Operetta and Sofia Pro

Colors
0054AA
0677BA
7BADD7
CADEEF
E8F1F8

Requirements
Must have
• Clean professional design that ties in closely to complement and extend the design elements in my website: marlowadvises.com
Nice to have
• Address and contact details I can edit in Microsoft Word, Outlook for Mac, etc
Should not have
• Excessive brand elements, fussy design and additional colours.

```html
<!DOCTYPE html>
<html lang="en">
<head>
<meta charset="utf-8">
<title>Marlow Advises — Business Card</title>
<link rel="stylesheet" href="https://fonts.googleapis.com/css2?family=Cormorant+Garamond:wght@500&family=Open+Sans:wght@400;700&display=swap">
<style>
  :root {
    --brand-navy: #2b3a86;
    --brand-navy-deep: #26337a;
    --paper-white: #ffffff;
    --backdrop: #e9ebf0;
    --card-shadow: rgba(20, 26, 60, 0.22);
  }
  * { box-sizing: border-box; margin: 0; padding: 0; }
  html, body {
    width: 1200px; height: 900px; overflow: hidden;
    background: var(--backdrop);
  }
  .canvas { position: relative; width: 1200px; height: 900px; }

  .card {
    position: absolute;
    width: 620px; height: 354px;
    border-radius: 16px;
    overflow: hidden;
    box-shadow: 0 14px 30px var(--card-shadow);
  }

  /* Front */
  .card-front {
    left: 470px; top: 60px;
    background: linear-gradient(135deg, var(--brand-navy-deep), var(--brand-navy) 60%, #33438f);
    display: flex; align-items: center; justify-content: center;
  }
  .brand-name {
    font-family: "Cormorant Garamond", serif;
    font-weight: 500;
    letter-spacing: 1px;
    white-space: nowrap;
  }
  .card-front .brand-name { color: var(--paper-white); font-size: 50px; }

  /* Back */
  .card-back { left: 130px; top: 470px; background: var(--paper-white); }
  .card-back svg.shapes { position: absolute; inset: 0; }
  .card-back .shape { fill: var(--brand-navy); }

  .contact-panel {
    position: absolute; left: 40px; top: 72px;
    color: var(--paper-white);
    font-family: "Open Sans", sans-serif;
  }
  .person-name { font-size: 23px; font-weight: 700; line-height: 1.1; }
  .person-role { font-size: 14px; margin-top: 2px; }
  .divider { width: 22px; height: 2px; background: var(--paper-white); margin: 14px 0; }
  .address { font-size: 14px; line-height: 1.35; }
  .contact-list { list-style: none; font-size: 15px; }
  .contact-list li { display: flex; align-items: center; gap: 10px; margin-bottom: 4px; }
  .contact-list svg { width: 13px; height: 13px; flex: none; }

  .card-back .brand-name {
    position: absolute; left: 330px; top: 150px; width: 270px;
    text-align: center; color: var(--brand-navy); font-size: 40px;
  }
</style>
</head>
<body>
<main class="canvas">

  <section class="card card-front" aria-label="Business card front">
    <span class="brand-name">Marlow Advises</span>
  </section>

  <section class="card card-back" aria-label="Business card back">
    <svg class="shapes" viewBox="0 0 620 354" width="620" height="354" aria-hidden="true">
      <polygon class="shape" points="0,0 230,0 380,354 0,354"/>
      <polygon class="shape" points="302,160 392,354 410,354"/>
    </svg>

    <div class="contact-panel">
      <p class="person-name">Daniel Hartley</p>
      <p class="person-role">Manager</p>
      <div class="divider"></div>
      <p class="address">Your address, city<br>state, ZIP 0000</p>
      <div class="divider"></div>
      <ul class="contact-list">
        <li>
          <svg viewBox="0 0 24 24" aria-hidden="true"><path fill="#fff" d="M6.6 10.8a15.1 15.1 0 0 0 6.6 6.6l2.2-2.2a1 1 0 0 1 1-.25 11.4 11.4 0 0 0 3.6.57 1 1 0 0 1 1 1V20a1 1 0 0 1-1 1A17 17 0 0 1 3 4a1 1 0 0 1 1-1h3.5a1 1 0 0 1 1 1c0 1.25.2 2.45.57 3.57a1 1 0 0 1-.25 1z"/></svg>
          123-456-2100
        </li>
        <li>
          <svg viewBox="0 0 24 24" aria-hidden="true"><path fill="#fff" d="M2 5h20v14H2zm2 2v.5l8 5 8-5V7z"/></svg>
          youremail@mailbox.com
        </li>
        <li>
          <svg viewBox="0 0 24 24" aria-hidden="true"><circle cx="12" cy="12" r="10" fill="#fff"/><path d="M2 12h20M12 2c3 3 3 17 0 20M12 2c-3 3-3 17 0 20" stroke="#2b3a86" stroke-width="1.5" fill="none"/></svg>
          www.yourwebsite.com
        </li>
      </ul>
    </div>

    <span class="brand-name">Marlow Advises</span>
  </section>

</main>
</body>
</html>
```